Redfield interiors PTY LTD

My business specializes in commercial fitout which builds walls, ceilings, doors, uses also materials aluminium in works. Id like to have a logo designed for my company too.

Industry/Entity Type

Business

```html
<!DOCTYPE html>
<html lang="en">
<head>
<meta charset="utf-8">
<title>Redfield Interiors – Business Cards</title>
<link href="https://fonts.googleapis.com/css2?family=Poppins:wght@600&family=Roboto:wght@300;500&display=swap" rel="stylesheet">
<style>
  :root {
    --stage: #1f1f21;
    --blue-top: #0670b8;
    --blue-bottom: #2b3479;
    --brand-blue: #1d4f9c;
    --ink-grey: #8a8a8a;
    --paper: #ffffff;
    --faint-ring-front: rgba(255,255,255,0.12);
    --faint-ring-back: #e9ebf4;
    --divider: #b8bcc6;
  }
  * { margin: 0; padding: 0; box-sizing: border-box; }
  html, body { width: 1189px; height: 1200px; overflow: hidden; }
  body { background: var(--stage); position: relative; font-family: "Roboto", Arial, sans-serif; }

  .card { position: absolute; left: 171px; width: 857px; height: 490px; overflow: hidden; }
  .card-front { top: 66px; background: linear-gradient(180deg, var(--blue-top) 0%, var(--blue-bottom) 100%); }
  .card-back { top: 625px; background: var(--paper); }

  .card svg.rings { position: absolute; inset: 0; width: 100%; height: 100%; }

  .wordmark { position: absolute; line-height: 1; }
  .wordmark .name {
    display: block; font-family: "Poppins", Arial, sans-serif; font-weight: 600;
    font-size: 48px; letter-spacing: 0.13em;
  }
  .wordmark .descriptor {
    display: block; font-family: "Roboto", Arial, sans-serif; font-weight: 300;
    font-size: 25px; letter-spacing: 0.26em; margin-top: 2px;
  }

  .card-front .wordmark { left: 336px; top: 205px; color: var(--paper); }

  .front-url {
    position: absolute; left: 0; right: 0; top: 410px; text-align: center;
    color: var(--paper); font-size: 20px; letter-spacing: 0.42em; font-weight: 300;
  }

  .side-band {
    position: absolute; left: 0; top: 0; width: 109px; height: 100%;
    background: linear-gradient(180deg, var(--blue-top) 0%, var(--blue-bottom) 100%);
  }
  .side-rule { position: absolute; left: 110px; top: 0; width: 3px; height: 100%; background: var(--divider); }

  .card-back .wordmark { left: 198px; top: 70px; }
  .card-back .wordmark .name { color: var(--brand-blue); }
  .card-back .wordmark .descriptor { color: var(--ink-grey); }

  .contact { position: absolute; left: 202px; top: 240px; color: var(--ink-grey); }
  .contact .person { font-weight: 500; font-size: 26px; line-height: 1; }
  .contact .role { color: var(--brand-blue); font-size: 23px; line-height: 1; margin-top: 2px; font-weight: 300; }
  .contact .address { font-size: 22px; line-height: 27px; margin-top: 18px; font-weight: 300; }
  .contact .lines { list-style: none; margin-top: 16px; }
  .contact .lines li { display: flex; align-items: center; font-size: 21px; font-weight: 300; height: 28px; }
  .contact .lines svg { width: 24px; height: 24px; margin-right: 9px; flex: none; }
</style>
</head>
<body>

<section class="card card-front">
  <svg class="rings" viewBox="0 0 857 490" aria-hidden="true">
    <circle cx="133" cy="242" r="245" fill="none" stroke="var(--faint-ring-front)" stroke-width="8"/>
    <circle cx="245" cy="243" r="58" fill="none" stroke="#ffffff" stroke-width="3"/>
  </svg>
  <div class="wordmark">
    <span class="name">REDFIELD</span>
    <span class="descriptor">INTERIORS PTY LTD</span>
  </div>
  <p class="front-url">www.redfieldinteriors.com</p>
</section>

<section class="card card-back">
  <svg class="rings" viewBox="0 0 857 490" aria-hidden="true">
    <circle cx="723" cy="244" r="259" fill="none" stroke="var(--faint-ring-back)" stroke-width="9"/>
  </svg>
  <div class="side-band"></div>
  <div class="side-rule"></div>
  <svg class="rings" viewBox="0 0 857 490" aria-hidden="true">
    <circle cx="109" cy="109" r="72" fill="#ffffff"/>
    <circle cx="109" cy="109" r="57" fill="none" stroke="var(--brand-blue)" stroke-width="3"/>
  </svg>
  <div class="wordmark">
    <span class="name">REDFIELD</span>
    <span class="descriptor">INTERIORS PTY LTD</span>
  </div>

  <div class="contact">
    <p class="person">LIAM CARTER</p>
    <p class="role">Founder</p>
    <p class="address">PO BOX 482 Harlow Lane<br>7 Kestrel Road Eastvale</p>
    <ul class="lines">
      <li>
        <svg viewBox="0 0 24 24" aria-hidden="true"><circle cx="12" cy="12" r="10.5" fill="none" stroke="var(--brand-blue)" stroke-width="1.6"/><path d="M7 10c0-2 10-2 10 0v1h-3v-1h-4v1H7z M8 12h8l1 5H7z" fill="var(--brand-blue)"/></svg>
        (555) 014-2368
      </li>
      <li>
        <svg viewBox="0 0 24 24" aria-hidden="true"><circle cx="12" cy="12" r="10.5" fill="none" stroke="var(--brand-blue)" stroke-width="1.6"/><rect x="6.5" y="8" width="11" height="8" fill="var(--brand-blue)"/><path d="M6.5 8l5.5 4.5L17.5 8" fill="none" stroke="#fff" stroke-width="1.2"/></svg>
        hello@redfieldmail.com
      </li>
      <li>
        <svg viewBox="0 0 24 24" aria-hidden="true"><circle cx="12" cy="12" r="10.5" fill="none" stroke="var(--brand-blue)" stroke-width="1.6"/><circle cx="12" cy="12" r="6" fill="none" stroke="var(--brand-blue)" stroke-width="1.2"/><path d="M6 12h12M12 6v12M8 8.5h8M8 15.5h8" stroke="var(--brand-blue)" stroke-width="1"/></svg>
        www.redfieldinteriors.com
      </li>
    </ul>
  </div>
</section>

</body>
</html>
```